businesscard, flyer and membercard

--------------------------------------------------------------------------------------------------
design flyer :
- delivering format (jpg, pdf and original psd)
- there is a example how the flyers should look like
the text and logo should be the same as the exemple flyer, the creativity is yours.
- the design should have a back and front side.
File format : 15,0 cm x 21,2 cm
design membercard :
- there is example how the member-card should look like
the text and logo should be the same as the exemple membercard, the creativity is yours.
- the front side contains text and open space where for writing :
Naam ......
Dansstijlen ......
- the front side contains 12 circels horizontal at the line name at the end of the line "Salsa".
- the front side contains 12 circels horizontal at the line name at the end of the line "Bachata".
- the front side contains 12 circels horizontal at the line name at the end of the line "Kizomba".
- each horizontal line with circels contains a different kind of color/design.
- file format: 7,6 cm x 10,7 cm
Business card :
- there is example how the businesscard should look like
the text and logo should be the same as the exemple buisinesscard, the creativity is yours.
- the design should have a back a front side
File format : 8,7 cm x 5,7 cm

Target Market(s)

Dancing :Salsa, Bachata and Kizomba

Colors

Designer to choose colors to be used in the design.

Requirements
Must have
• same text as seen on the examples.
Nice to have
• see the examples as attachments
Should not have
• - REMOVE TEXT "KOV" from the design
• - REMOVE TEXT "Gratis Parkeren"

```html
<!DOCTYPE html>
<html lang="nl">
<head>
<meta charset="utf-8">
<title>Solara Dance Studio – Flyer voor- en achterkant</title>
<link rel="stylesheet" href="https://fonts.googleapis.com/css2?family=Montserrat:wght@500;600;700&family=Quicksand:wght@500;600&family=Cinzel:wght@700&display=swap">
<style>
  :root {
    --stage: #3a3f44;
    --flyer-black: #0b0a0a;
    --white: #ffffff;
    --red: #e0262b;
    --dancer-red: #c42a2e;
    --dancer-dark: #1c1414;
  }
  * { margin: 0; padding: 0; box-sizing: border-box; }
  html, body { width: 1200px; height: 1200px; overflow: hidden; }
  body {
    background: var(--stage);
    font-family: "Montserrat", sans-serif;
    color: var(--white);
    position: relative;
  }
  .flyer {
    position: absolute;
    top: 220px;
    width: 538px;
    height: 758px;
    background: var(--flyer-black);
    overflow: hidden;
  }
  .flyer--front { left: 44px; }
  .flyer--back { left: 630px; }
  .flyer__backdrop { position: absolute; inset: 0; }
  .flyer--front .flyer__backdrop {
    background:
      radial-gradient(ellipse 75% 50% at 50% 30%, rgba(200,146,58,.5), rgba(90,60,30,.3) 60%, transparent 85%),
      linear-gradient(180deg, #3b2b18 0%, #1a140d 60%, var(--flyer-black) 100%);
  }
  .flyer--back .flyer__backdrop {
    background:
      radial-gradient(ellipse 80% 45% at 50% 25%, rgba(120,95,60,.45), transparent 75%),
      linear-gradient(180deg, #2c241b 0%, #15110d 50%, var(--flyer-black) 100%);
  }
  .abs { position: absolute; }
  .center { text-align: center; }

  /* Front */
  .dancers-photo {
    left: 122px; top: 110px; width: 290px; height: 416px;
    border-radius: 6px;
    background:
      linear-gradient(100deg, var(--dancer-dark) 0%, #2a1c1c 42%, #8e2226 58%, var(--dancer-red) 78%, #7a1e22 100%);
  }
  .headline-box {
    left: 46px; top: 22px; width: 450px; height: 110px;
    border: 2px solid var(--white);
  }
  .headline-box__title {
    position: absolute; left: 0; right: 0; top: 10px;
    font-weight: 700; font-size: 33px; letter-spacing: .5px;
  }
  .headline-box__rule {
    position: absolute; left: 78px; width: 290px; top: 51px; height: 2px;
    background: var(--white);
  }
  .headline-box__dates {
    position: absolute; left: 0; right: 0; top: 58px;
    font-weight: 700; font-size: 33px;
  }
  .style-arc { left: 0; top: 0; width: 538px; height: 758px; }
  .style-arc text {
    font-family: "Cinzel", serif; font-weight: 700; font-size: 30px;
    fill: var(--white); letter-spacing: 1px;
  }
  .perks-box {
    left: 164px; top: 340px; width: 210px; height: 150px;
    border: 2px solid var(--white);
    background: rgba(0,0,0,.25);
    padding-top: 18px;
    font-weight: 500; font-size: 18.5px; line-height: 28px;
  }
  .brand-box {
    border: 2px solid var(--white);
    background: rgba(0,0,0,.6);
    display: flex; flex-direction: column; align-items: center; justify-content: center;
    gap: 10px;
  }
  .brand-box--front { left: 142px; top: 528px; width: 258px; height: 212px; }
  .brand-box__name, .brand-box__sub { font-weight: 600; color: var(--white); }
  .brand-box__name { font-size: 40px; letter-spacing: 6px; }
  .brand-box__sub { font-size: 20px; letter-spacing: 1px; }

  /* Back */
  .first-lesson-badge {
    left: 18px; top: 14px; width: 120px; height: 120px;
    border: 1.5px solid var(--white); border-radius: 50%;
    display: flex; align-items: center; justify-content: center;
    font-weight: 600; font-size: 18px; line-height: 20px;
  }
  .venue-name {
    left: 196px; top: 16px; width: 180px;
    color: var(--red); font-weight: 700; font-size: 18px;
  }
  .schedule-title { left: 162px; top: 86px; font-weight: 700; font-size: 31px; }
  .schedule-day { top: 160px; width: 180px; }
  .schedule-day__name { font-weight: 700; font-size: 20px; margin-bottom: 4px; }
  .schedule-day__slot { font-family: "Quicksand", sans-serif; font-weight: 500; font-size: 16.5px; line-height: 20.5px; }
  .style-row {
    left: 0; right: 0; top: 288px;
    display: flex; justify-content: center; gap: 26px;
    font-weight: 700; font-size: 30px;
  }
  .brand-box--back { left: 153px; top: 362px; width: 237px; height: 196px; }
  .brand-box--back .brand-box__name { font-size: 36px; letter-spacing: 5px; }
  .brand-box--back .brand-box__sub { font-size: 18px; }
  .couple-illustration {
    top: 384px; width: 124px; height: 142px;
    border-radius: 6px;
    background: linear-gradient(160deg, var(--dancer-red) 0%, #a32226 55%, #5a1416 100%);
  }
  .contact {
    left: 0; right: 0; font-size: 21px;
    display: flex; justify-content: center; align-items: center; gap: 6px;
    font-family: "Quicksand", sans-serif; font-weight: 600;
  }
  .contact svg { flex: none; }
  .contact__square { width: 14px; height: 14px; background: var(--red); flex: none; }
  .footer-rule { height: 2px; background: var(--white); }
</style>
</head>
<body>

<section class="flyer flyer--front" aria-label="Voorkant flyer">
  <div class="flyer__backdrop" role="img" aria-label="Donkere achtergrond met gouden en gekleurde stippen en silhouetten van palmbomen"></div>
  <div class="abs dancers-photo" role="img" aria-label="Foto van een dansend paar, man in zwart pak en vrouw in rode jurk"></div>

  <div class="abs headline-box center">
    <div class="headline-box__title">GRATIS PROEFLESSEN</div>
    <div class="headline-box__rule"></div>
    <div class="headline-box__dates">26 T/M 28 Sept</div>
  </div>

  <svg class="abs style-arc" viewBox="0 0 538 758">
    <path id="styleArcPath" d="M 56 410 Q 270 165 494 410" fill="none"/>
    <text><textPath href="#styleArcPath" startOffset="15%" text-anchor="middle">SALSA</textPath></text>
    <text><textPath href="#styleArcPath" startOffset="49%" text-anchor="middle">BACHATA</textPath></text>
    <text><textPath href="#styleArcPath" startOffset="85%" text-anchor="middle">KIZOMBA</textPath></text>
  </svg>

  <div class="abs perks-box center">
    Eerste Les Gratis<br>Student Korting<br>Elk niveau<br>Alle leeftijden
  </div>

  <div class="abs brand-box brand-box--front">
    <div class="brand-box__name">SOLARA</div>
    <div class="brand-box__sub">DANCE STUDIO</div>
  </div>
</section>

<section class="flyer flyer--back" aria-label="Achterkant flyer">
  <div class="flyer__backdrop" role="img" aria-label="Donkere achtergrond met stippen, palmbomen, vogels en rook"></div>

  <div class="abs first-lesson-badge center">Eerste Les<br>Gratis</div>
  <div class="abs venue-name center">CLUB MARVENTO</div>
  <div class="abs schedule-title">LES ROOSTER</div>

  <div class="abs schedule-day center" style="left:-1px">
    <div class="schedule-day__name">DINSDAG</div>
    <div class="schedule-day__slot">19:00 Salsa 1</div>
    <div class="schedule-day__slot">20:00 Salsa 3</div>
    <div class="schedule-day__slot">21:00 Bachata 3</div>
  </div>
  <div class="abs schedule-day center" style="left:176px">
    <div class="schedule-day__name">WOENSDAG</div>
    <div class="schedule-day__slot">19:00 Kizomba 2</div>
    <div class="schedule-day__slot">20:00 Kizomba 1</div>
    <div class="schedule-day__slot">21:00 Kizomba 3</div>
  </div>
  <div class="abs schedule-day center" style="left:352px">
    <div class="schedule-day__name">DONDERDAG</div>
    <div class="schedule-day__slot">19:00 Salsa2</div>
    <div class="schedule-day__slot">20:00 Bachata 1</div>
    <div class="schedule-day__slot">21:00 Bachata 2</div>
  </div>

  <div class="abs style-row"><span>SALSA</span><span>BACHATA</span><span>KIZOMBA</span></div>

  <div class="abs couple-illustration" style="left:10px" role="img" aria-label="Rode illustratie van een dansend paar"></div>
  <div class="abs couple-illustration" style="left:402px" role="img" aria-label="Rode illustratie van een dansend paar"></div>

  <div class="abs brand-box brand-box--back">
    <div class="brand-box__name">SOLARA</div>
    <div class="brand-box__sub">DANCE STUDIO</div>
  </div>

  <div class="abs contact" style="top:576px">
    <svg width="14" height="20" viewBox="0 0 14 20"><path d="M7 0a7 7 0 0 0-7 7c0 5 7 13 7 13s7-8 7-13a7 7 0 0 0-7-7zm0 10a3 3 0 1 1 0-6 3 3 0 0 1 0 6z" fill="var(--red)"/></svg>
    <span>Parkweg 42, 2514 AB</span>
  </div>
  <div class="abs contact" style="top:600px"><span>Den Haag</span></div>
  <div class="abs contact" style="top:638px">
    <svg width="18" height="14" viewBox="0 0 18 14"><path d="M1 4c0-2 3-4 8-4s8 2 8 4v2h-4V4H5v2H1z M3 7h12l2 7H1z" fill="var(--red)"/></svg>
    <span>0620418837</span>
  </div>
  <div class="abs contact" style="top:676px">
    <span class="contact__square"></span>
    <span>Solaradenhaag</span>
  </div>

  <div class="abs footer-rule" style="left:33px;top:723px;width:138px"></div>
  <div class="abs footer-rule" style="left:200px;top:723px;width:138px"></div>
  <div class="abs footer-rule" style="left:366px;top:723px;width:139px"></div>
  <div class="abs footer-rule" style="left:232px;top:734px;width:73px"></div>
</section>

</body>
</html>
```